Toner cartridge manufacturer needs stunning "Green" box design

We distribute environmentally friendly, premium, high quality re-manufactured toner cartridges. As a national wholesale Distributor, we ship products everyday all over the country and have a huge variety of customers and products. Part of our product offering is a Premium Toner Cartridge and we need a new, striking and beautifully simple box design. This box should have an emphasis on being "Green" and imply environmental friendliness. This Premium Toner Cartridge offering will not have a name brand and the box should ultimately be generic. We would like to see a well laid out 4 panel box(front, back, sides, top). There should be a continual theme and design that is consistent throughout the whole box. The front of the box should have the primary design that carries over to the other sides. Eye catching graphics and a space in the lower right hand corner for a label to be wrapped around the corner. In another corner on the front, there should be text that reads "Premium Toner Cartridge". This text should not be the focus and not take up very much space. The back panel will carry the theme over that's on the front but there will need to be 4 boxes/sections for text to describe the premium toner cartridge. The sides would allow for small logo/graphics, disclaimers and the second part of the wrap label described on the lower right hand side of the front of the box. Please look at QD, Brondil, Tuvan and other OEM toner boxes to gather inspiration for our desired overall look and feel. Please refrain from using stock art/stock images that will be easily identified or frequently used.

The attached image is a design that was previously done. We would like to see creative expansions similar to this. The layout is preferred as far as the label area and text on the back panel. The circle design on this is something we dont line. Instead graphics that emphasize the environment and being "green" are preferred. Use of the design to fill in more unused are would be nice.

Hi All,

Thanks for your designs.

The color green is not necessarily desired.  Sorry for the confusion.  Many boxes we see today are green in color and that will make it difficult for us to stand out.   

• stock graphics, common images that would be easily seen in other designs(literature, packaging, advertising)

```html
<!DOCTYPE html>
<html lang="en">
<head>
<meta charset="utf-8">
<title>Premium Toner Cartridge – Box Dieline</title>
<link href="https://fonts.googleapis.com/css2?family=Questrial&family=Roboto:wght@400;700&display=swap" rel="stylesheet">
<style>
  :root {
    --box-blue: #00aeef;
    --box-navy: #003a57;
    --leaf-green: #6ab023;
    --icon-cyan: #33c6f4;
    --label-grey: rgba(215, 215, 215, 0.7);
    --cut-line: #8a8a8a;
    --text-dark: #1a1a1a;
    --paper: #ffffff;
  }
  * { margin: 0; padding: 0; box-sizing: border-box; }
  html, body { width: 1200px; height: 1000px; overflow: hidden; background: var(--paper); }
  .canvas { position: relative; width: 1200px; height: 1000px; }
  .dieline { position: absolute; inset: 0; }
  .front-title {
    position: absolute; left: 51px; top: 437px;
    font-family: "Questrial", sans-serif; font-size: 16px; color: var(--box-blue);
    letter-spacing: 0.2px;
  }
  .top-title {
    position: absolute; left: 785px; top: 357px; width: 220px;
    font-family: "Questrial", sans-serif; font-size: 15px; color: var(--paper);
    transform: rotate(180deg); transform-origin: center; white-space: nowrap;
  }
  .feature {
    position: absolute; top: 457px; width: 84px;
    font-family: "Roboto", sans-serif; color: var(--text-dark);
  }
  .feature-badge {
    display: block; width: 70px; height: 70px; margin-bottom: 4px;
  }
  .feature-heading {
    background: var(--box-blue); color: var(--paper);
    font-size: 6.2px; font-weight: 700; line-height: 7.4px;
    padding: 1px 3px; min-height: 17px; margin-bottom: 5px;
  }
  .feature-copy {
    font-size: 6.1px; font-weight: 700; line-height: 7.3px;
    text-align: justify;
  }
</style>
</head>
<body>
<div class="canvas">
  <svg class="dieline" width="1200" height="1000" viewBox="0 0 1200 1000" xmlns="http://www.w3.org/2000/svg">
    <defs>
      <linearGradient id="labelBar" x1="0" x2="1">
        <stop offset="0" stop-color="#7cc242"/>
        <stop offset="1" stop-color="#00aeef"/>
      </linearGradient>
      <linearGradient id="cubeTones" x1="0" y1="0" x2="1" y2="1">
        <stop offset="0" stop-color="#f06bb5"/>
        <stop offset="0.35" stop-color="#ffb43a"/>
        <stop offset="0.6" stop-color="#2e8fdc"/>
        <stop offset="1" stop-color="#e0479e"/>
      </linearGradient>
      <linearGradient id="greenCube" x1="0" y1="0" x2="1" y2="1">
        <stop offset="0" stop-color="#c7ee7a"/>
        <stop offset="1" stop-color="#6cbf1c"/>
      </linearGradient>
    </defs>

    <!-- glue flap -->
    <polygon class="glue-flap" points="5,408 36,400 36,688 5,680" fill="#fff" stroke="var(--cut-line)" stroke-width="0.8"/>

    <!-- hang tab -->
    <path class="hang-tab" d="M204,400 V382 Q204,372 214,372 H258 Q268,372 268,382 V400" fill="#fff" stroke="var(--cut-line)" stroke-width="0.8"/>
    <path class="hang-hole" d="M222,400 V392 A14,14 0 0 1 250,392 V400" fill="none" stroke="var(--cut-line)" stroke-width="0.8"/>

    <!-- front panel -->
    <rect class="front-panel" x="36" y="400" width="399" height="288" fill="#fff" stroke="var(--cut-line)" stroke-width="0.8"/>
    <rect class="front-graphic" role="img" aria-label="Colourful translucent floating cubes in pink, orange and blue" x="40" y="555" width="228" height="133" rx="10" fill="url(#cubeTones)" opacity="0.85"/>
    <rect class="front-graphic" role="img" aria-label="Translucent lime green cube" x="302" y="497" width="62" height="84" rx="8" fill="url(#greenCube)"/>
    <rect class="label-area" x="231" y="544" width="366" height="128" fill="var(--label-grey)"/>
    <rect class="label-bar" x="231" y="669" width="366" height="6" fill="url(#labelBar)"/>

    <!-- side panel one -->
    <polygon class="dust-flap" points="435,400 435,390 445,355 617,355 617,400" fill="var(--box-blue)"/>
    <line x1="435" y1="400" x2="435" y2="688" stroke="var(--cut-line)" stroke-width="0.8"/>
    <g class="handling-icons" fill="var(--leaf-green)">
      <circle cx="478" cy="445" r="10"/><circle cx="502" cy="445" r="10"/><circle cx="526" cy="445" r="10"/><circle cx="550" cy="445" r="10"/><circle cx="575" cy="445" r="10"/>
    </g>
    <g class="handling-glyphs" fill="none" stroke="#fff" stroke-width="1.4" stroke-linecap="round">
      <path d="M471,444 A7,6 0 0 1 485,444 Z M478,444 V451"/>
      <path d="M497,440 H507 L502,446 Z M502,446 V451 M499,451 H505"/>
      <path d="M526,439 L520,445 H523 V451 H529 V445 H532 Z"/>
      <circle cx="550" cy="445" r="3"/><path d="M550,437 V439 M550,451 V453 M542,445 H544 M556,445 H558"/>
      <path d="M570,449 L575,440 L580,449 Z"/>
    </g>

    <!-- top panel -->
    <path class="top-panel" d="M617,400 V197 Q617,185 629,185 H1005 Q1017,185 1017,197 V400 Z" fill="var(--box-blue)"/>
    <rect class="top-notch" x="785" y="208" width="63" height="10" fill="none" stroke="var(--box-navy)" stroke-width="0.8"/>
    <path d="M805,208 A11,6 0 0 0 827,208" fill="none" stroke="var(--box-navy)" stroke-width="0.8"/>

    <!-- back panel -->
    <rect class="back-panel" x="617" y="400" width="400" height="288" fill="#fff" stroke="var(--cut-line)" stroke-width="0.8"/>

    <!-- side panel two -->
    <polygon class="dust-flap" points="1017,218 1160,218 1197,400 1017,400" fill="var(--box-blue)"/>
    <rect class="side-panel" x="1017" y="400" width="180" height="288" fill="var(--box-blue)"/>
    <g class="handling-icons" fill="var(--icon-cyan)" stroke="#fff" stroke-width="0.6">
      <circle cx="1058" cy="445" r="10"/><circle cx="1083" cy="445" r="10"/><circle cx="1108" cy="445" r="10"/><circle cx="1133" cy="445" r="10"/><circle cx="1157" cy="445" r="10"/>
    </g>
    <g class="handling-glyphs" fill="none" stroke="#fff" stroke-width="1.4" stroke-linecap="round">
      <path d="M1051,444 A7,6 0 0 1 1065,444 Z M1058,444 V451"/>
      <path d="M1078,440 H1088 L1083,446 Z M1083,446 V451 M1080,451 H1086"/>
      <path d="M1108,439 L1102,445 H1105 V451 H1111 V445 H1114 Z"/>
      <circle cx="1133" cy="445" r="3"/><path d="M1133,437 V439 M1133,451 V453 M1125,445 H1127 M1139,445 H1141"/>
      <path d="M1152,449 L1157,440 L1162,449 Z"/>
    </g>

    <!-- bottom flaps -->
    <polygon class="bottom-flap" points="36,688 435,688 357,776 114,776" fill="var(--box-blue)"/>
    <rect class="bottom-tuck" x="114" y="776" width="243" height="39" fill="var(--box-navy)"/>

    <polygon class="bottom-flap" points="435,688 617,688 617,705 527,765 527,815 435,815" fill="var(--box-blue)"/>
    <polygon points="435,690 508,815 435,815" fill="var(--box-navy)"/>

    <polygon class="bottom-flap" points="617,688 1017,688 1017,815 932,815 932,763 707,763 707,815 617,815" fill="var(--box-blue)"/>
    <polygon points="617,690 707,815 617,815" fill="var(--box-navy)"/>
    <polygon points="1017,690 1017,815 932,815" fill="var(--box-navy)"/>

    <polygon class="bottom-flap" points="1017,688 1197,688 1197,815 1108,815 1108,760 1017,700" fill="var(--box-blue)"/>
    <polygon points="1197,690 1197,815 1108,815" fill="var(--box-navy)"/>

    <!-- back panel footer marks -->
    <circle cx="812" cy="718" r="5" fill="#555"/>
    <circle cx="829" cy="718" r="6" fill="var(--leaf-green)"/>
    <path d="M826,720 L829,714 L832,720 Z" fill="none" stroke="#fff" stroke-width="1"/>
  </svg>

  <p class="front-title">PREMIUM TONER CARTRIDGE</p>
  <p class="top-title">PREMIUM TONER CARTRIDGE</p>

  <section class="feature" style="left:628px">
    <svg class="feature-badge" viewBox="0 0 70 70"><rect x="0.5" y="0.5" width="69" height="69" rx="6" fill="#fff" stroke="#ddd"/><circle cx="35" cy="35" r="24" fill="#222"/></svg>
    <h3 class="feature-heading">100% Satisfaction Guaranteed</h3>
    <p class="feature-copy">Your complete satisfaction is guaranteed on all Premium Toner Cartridges and is backed by a 5 year warranty. We guarantee that your cartridge will be free from defects in material and workmanship and is 100% compatible for the printer of which it was intended.</p>
  </section>

  <section class="feature" style="left:726px">
    <svg class="feature-badge" viewBox="0 0 70 70"><rect x="0.5" y="0.5" width="69" height="69" rx="6" fill="#fff" stroke="#ddd"/><circle cx="35" cy="33" r="24" fill="#2a6fb8"/></svg>
    <h3 class="feature-heading">Dependable Quality and Worry Free Performance</h3>
    <p class="feature-copy">Enjoy complete confidence that quality and performance will meet or exceed that of the OEM. Guaranteed page yields and reliability keeps customers printing happy with reliable printer performance. See the difference for yourself! 100% chemical toner produces vibrant and exceptional color prints. The highest quality mono toner keeps mono prints coming out crisp and consistent.</p>
  </section>

  <section class="feature" style="left:824px">
    <svg class="feature-badge" viewBox="0 0 70 70"><rect x="0.5" y="0.5" width="69" height="69" rx="6" fill="#fff" stroke="#ddd"/><rect x="12" y="14" width="46" height="42" fill="#222"/></svg>
    <h3 class="feature-heading">PTCA Compliant and QMS Certified</h3>
    <p class="feature-copy">Utilizing only OEM cores and premium non-IP infringing components, the quality and performance will exceed expectations. The remanufacturing process includes installation of new long life drums, premium matched toners, new blades and seals, PCR's, magnetic rollers and new smart chips.</p>
  </section>

  <section class="feature" style="left:921px">
    <svg class="feature-badge" viewBox="0 0 70 70"><rect x="0.5" y="0.5" width="69" height="69" rx="6" fill="#fff" stroke="#ddd"/><circle cx="35" cy="32" r="22" fill="var(--leaf-green)"/></svg>
    <h3 class="feature-heading">Easy Recycling and Environmentally Responsible</h3>
    <p class="feature-copy">Our closed loop recycling and reuse program minimizes environmental impact and makes recycling your empty cartridges easy and painless. Simply collect your empty cartridges in one of our ready to ship recycle boxes and when its full, simply give it to your ParcelGo driver or location and send it back on the provided return label. IT'S THAT EASY!</p>
  </section>
</div>
</body>
</html>
```